Research Report on Media Literacy Needs a Design

We've got a cool story to tell about an innovative process of teacher professional development in media literacy education. We have a 20 page report about the work. We're looking for a designer to give it a simple but attractive look so we can publish it online.

Teacher

```html
<!DOCTYPE html>
<html lang="en">
<head>
<meta charset="utf-8">
<title>Media and Information Literacy – Page 04</title>
<link href="https://fonts.googleapis.com/css2?family=Lato:ital,wght@0,400;0,700;1,400&family=Raleway:wght@500&display=swap" rel="stylesheet">
<style>
  :root {
    --ink: #2b2b2b;
    --accent: #2f93d3;
    --quote-bg: #3399d6;
    --paper: #ffffff;
  }
  html, body { margin: 0; padding: 0; overflow: hidden; background: var(--paper); }
  .page {
    position: relative;
    width: 927px;
    height: 1200px;
    overflow: hidden;
    background: var(--paper);
    font-family: "Lato", Arial, sans-serif;
    color: var(--ink);
    font-size: 15px;
    line-height: 18.9px;
  }
  .block { position: absolute; margin: 0; }
  .indent { left: 91px; width: 774px; }
  .full { left: 64px; width: 800px; }
  .term { color: var(--accent); font-style: italic; }
  .tick { position: absolute; left: 64px; top: 277px; width: 16px; height: 14px; }
  .pull-quote { position: absolute; left: 72px; top: 526px; width: 783px; height: 145px; }
  .pull-quote svg { position: absolute; inset: 0; }
  .pull-quote p {
    position: absolute; left: 60px; top: 36px; width: 700px; margin: 0;
    color: #fff; font-size: 19.6px; line-height: 25.5px;
  }
  .qmark { position: absolute; color: #fff; font-family: Georgia, serif; font-size: 46px; line-height: 1; }
  .qmark.open { left: 36px; top: 32px; }
  .qmark.close { left: 663px; top: 93px; }
  .folio { position: absolute; left: 0; top: 1154px; width: 927px; height: 22px; }
  .folio .num {
    position: absolute; left: 0; top: 0; width: 70px; height: 21px;
    background: var(--accent); color: #fff; font-weight: 700; font-size: 15px;
    line-height: 21px; text-align: right; padding-right: 0; box-sizing: border-box; padding-right: 4px;
  }
  .folio .title {
    position: absolute; left: 77px; top: 1px; color: var(--accent);
    font-family: "Raleway", "Lato", sans-serif; font-weight: 500; font-size: 16px; letter-spacing: 0.2px;
  }
  .folio .rule { position: absolute; left: 403px; right: 0; top: 14px; height: 1px; background: var(--accent); }
</style>
</head>
<body>
<div class="page">
  <p class="block indent" style="top:151px">portant shifts occurred in the planning and implementation process, including the movement away from our intended plan of curriculum mapping and identification of learning targets to a more fluid, flexible and generative approach that used the identification of MIL in existing curriculum, lesson plan tagging, the blending of MIL with other competencies and literacies essential to learning at Harbor Lane School, and a committee-led share-out of ideas as a professional development program for the full faculty.</p>

  <svg class="tick" viewBox="0 0 16 14" aria-hidden="true"><path d="M1.5 7.5 L6 12 L14.5 2" fill="none" stroke="#2f93d3" stroke-width="2.6"/></svg>
  <p class="block indent" style="top:270px"><span class="term">The use of creative tactical strategies to accomplish practical goals through blended learning.</span> Rather than simply drop knowledge on Harbor Lane School faculty, the Literacy Studio Lab team worked to identify a clear and specific goal for the engagement, adjusting our own approaches to support collaboration. To sustain a six-month, bi-coastal partnership, this professional development program used blended learning that included two intensive face-to-face meetings and several forms of intense online engagement, including teleconferencing, cloud-based collaboration, and the use of online tagging taxonomies to extend learning outside the walls of Harbor Lane School and continue learning consistently between face-to-face sessions.</p>

  <p class="block full" style="top:434px">Our challenge was to support the Harbor Lane School faculty, enabling them to <span class="term">converge</span> on a suitable definition of media and information literacy, <span class="term">activate</span> their creative, collaborative development of lessons and projects informed by media and information literacy, and <span class="term">extend</span> any professional development insights into an ongoing process of building and sharing MIL practices across subjects and grade levels.</p>

  <figure class="pull-quote" style="margin:0">
    <svg viewBox="0 0 783 145" aria-hidden="true"><polygon points="30,0 783,0 783,118 755,145 0,145 0,30" fill="#3399d6"/></svg>
    <span class="qmark open">&#8216;</span>
    <p>Media and information literacy is an expanded conceptualization of literacy that includes the ability to access, analyze, compose, reflect and take action using media texts, tools and technologies in a wide variety of forms.</p>
    <span class="qmark close">&#8217;</span>
  </figure>

  <p class="block full" style="top:695px">In the process, we discovered the faculty’s existing understandings of media and information literacy and pushed them further within their own contexts. This process of discovery and flexibility required several key shifts from standard top-down professional development models and through a process Ellis and Brandt have called <span class="term">messy engagement</span>. When staff development (like other forms of teaching and learning) activates engagement, collaboration, creativity, innovation, and risk-taking, it can be messy at times. Rather than focusing on a product to be completed after a predetermined and linear course of learning and synthesis, messy engagement is exploratory and iterative. We believe that messy engagement is the only way to truly honor the individual motivations and passions that expert faculty in independent school settings exhibit.</p>

  <p class="block full" style="top:849px">This approach to professional development seemed to meet the needs of Harbor Lane School faculty. By taking ownership of the professional development process and being amenable to adjustments and new approaches as needed, the Harbor Lane School faculty ended up with a more customized and expansive vision for MIL integration that paved the way for collaborative development in the future. As one member of the MIL committee put it, “This is not something we could do anywhere. It worked with <span class="term">this</span> community. It was possible because of [our] sophisticated, experienced team members.”</p>

  <footer class="folio">
    <span class="num">Pg 04</span>
    <span class="title">MEDIA AND INFORMATION LITERACY</span>
    <span class="rule"></span>
  </footer>
</div>
</body>
</html>
```